Paperback Book Cover Design

I need a professional cover designed for my new book. You must use the design template enclosed. The title of the book is “Open Your Digital Purse Now!” The graphic used on the book cover should of course relate to making money online through various skills such as writing, graphic design, online marketing, photography, trading, Tradlo etc. The graphic(s) used must demonstrate to the reader that the book gives various ways to make money online.

At the top of the book you must include the sub heading “Earn From Home Collection”. The main title of the book is “Open Your Digital Purse Now!”, which of course should be highly prominent on the front cover. The front cover must also include the author name, Gerald Whitcombe.

I have no preference to colours used so do be creative to create an eye catching cover design.

The spine of the book should include the main title and the author name. Feel free to use an image or images for the rear of the book and just add dummy text.

The winning designer must supply a layered psd file complete with all fonts and elements used.

Industry/Entity Type

Graphic Design

Requirements
Must have
• The winning designer must supply a layered psd file complete with all fonts and elements used.

```html
<!DOCTYPE html>
<html lang="en">
<head>
<meta charset="utf-8">
<title>Open Your Digital Purse Now! — Paperback Cover</title>
<link rel="stylesheet" href="https://fonts.googleapis.com/css2?family=Teko:wght@500;600&family=Cinzel:wght@400&family=Tinos&family=Arimo:wght@400;700&display=swap">
<style>
  :root {
    --paper: #cfcfcf;
    --ink: #111111;
    --accent: #ff6a00;
    --glow: #ffffff;
    --photo-pink: #e879b8;
    --photo-grey: #bdbdbd;
    --body-ink: #222222;
    --marker: #fff200;
  }
  * { margin: 0; padding: 0; box-sizing: border-box; }
  html, body { width: 1200px; height: 867px; overflow: hidden; background: var(--paper); }
  .cover-sheet {
    position: relative;
    width: 1024px; height: 740px;
    background: var(--paper);
    transform: scale(1.171875);
    transform-origin: 0 0;
  }
  .display { font-family: "Teko", "Arial Narrow", sans-serif; font-weight: 600; text-transform: uppercase; line-height: 0.8; position: absolute; white-space: nowrap; text-align: center; }
  .accent { color: var(--accent); }
  .ink { color: var(--ink); }

  /* back cover */
  .back-title { left: 0; width: 516px; }
  .back-title.l1 { top: 80px; font-size: 66px; }
  .back-title.l2 { top: 130px; font-size: 62px; }
  .back-title.l3 { top: 198px; font-size: 114px; }
  .back-blurb {
    position: absolute; left: 73px; top: 305px; width: 374px;
    font-family: "Arimo", Arial, sans-serif; font-size: 11.6px; line-height: 18.4px;
    color: var(--body-ink); text-align: justify;
  }
  .author-photo { position: absolute; left: 75px; top: 452px; width: 86px; height: 123px; background: #ffffff; }
  .author-bio {
    position: absolute; left: 180px; top: 452px; width: 262px; height: 126px; overflow: hidden;
    font-family: "Tinos", "Times New Roman", serif; font-size: 11.8px; line-height: 15.4px;
    color: var(--body-ink); text-align: justify;
  }
  .author-bio .bio-name { font-size: 18px; }
  .barcode-area {
    position: absolute; left: 260px; top: 595px; width: 178px; height: 107px;
    background: var(--marker); display: flex; align-items: center; justify-content: center;
    font-family: "Arimo", Arial, sans-serif; font-weight: 700; font-size: 15px; line-height: 22px;
    text-align: center; color: #222;
  }

  /* spine */
  .spine {
    position: absolute; left: 495px; top: 45px; height: 660px; width: 32px;
    writing-mode: vertical-rl; display: flex; align-items: center; gap: 26px;
  }
  .spine-title { font-family: "Teko", sans-serif; font-weight: 600; font-size: 34px; line-height: 1; text-transform: uppercase; white-space: nowrap; color: var(--ink); }
  .spine-author { font-family: "Cinzel", serif; font-size: 22px; line-height: 1; white-space: nowrap; color: var(--ink); letter-spacing: 2px; }

  /* front cover */
  .series-line {
    position: absolute; left: 540px; width: 484px; top: 46px; text-align: center;
    font-family: "Teko", sans-serif; font-weight: 600; font-size: 32px; line-height: 1;
    letter-spacing: 2.5px; text-transform: uppercase; color: var(--ink);
  }
  .hero-glow {
    position: absolute; left: 560px; top: 80px; width: 430px; height: 310px;
    background: radial-gradient(ellipse at 50% 45%, var(--glow) 0%, rgba(255,255,255,0.7) 35%, rgba(255,255,255,0) 70%);
  }
  .hero-graphic {
    position: absolute; left: 655px; top: 148px; width: 225px; height: 162px; border-radius: 40px;
    background: linear-gradient(90deg, var(--photo-pink) 0%, var(--photo-pink) 52%, var(--photo-grey) 64%, #e6e6e6 100%);
  }
  .front-title { left: 540px; width: 484px; }
  .front-title.l1 { top: 385px; font-size: 86px; }
  .front-title.l2 { top: 452px; font-size: 82px; }
  .front-title.l3 { top: 543px; font-size: 128px; }
  .front-author {
    position: absolute; left: 540px; width: 484px; top: 652px; text-align: center;
    font-family: "Cinzel", serif; font-size: 35px; line-height: 1; letter-spacing: 2px; color: var(--ink);
  }
</style>
</head>
<body>
<div class="cover-sheet">

  <section class="back-cover">
    <div class="display back-title l1 ink">Open Your</div>
    <div class="display back-title l2 accent">Digital Purse</div>
    <div class="display back-title l3 ink">Now!</div>
    <p class="back-blurb">need a professional cover designed for my new book. You must use the design template enclosed. The title of the book is “Open Your Digital Purse Now!” The graphic used on the book cover should of course relate to making money online through various skills such as writing, graphic design, online marketing, photography, trading, Tradlo etc. The graphic(s) used must demonstrate to the reader that the book gives various ways to make money online.</p>
    <div class="author-photo"></div>
    <p class="author-bio"><span class="bio-name">Gerald Whitcombe</span> The title of the book is “Open Your Digital Purse Now!” The graphic used on the book cover should of course relate to making money online through various skills such as writing, graphic design, online marketing, photography, trading, Tradlo etc. The graphic(s) used must demonstrate to the reader that the book gives various ways to make m</p>
    <div class="barcode-area">Barcode<br>Location &amp; Size<br>2″ X 1.2″</div>
  </section>

  <section class="spine">
    <span class="spine-title">Open Your <span class="accent">Digital Purse</span> Now!</span>
    <span class="spine-author">Gerald Whitcombe</span>
  </section>

  <section class="front-cover">
    <div class="series-line">Earn From Home Collection</div>
    <div class="hero-glow"></div>
    <div class="hero-graphic" role="img" aria-label="Photo of a pink piggy bank plugged into a grey computer mouse"></div>
    <div class="display front-title l1 ink">Open Your</div>
    <div class="display front-title l2 accent">Digital Purse</div>
    <div class="display front-title l3 ink">Now!</div>
    <div class="front-author">Gerald Whitcombe</div>
  </section>

</div>
</body>
</html>
```